Home Page Design

We are refreshing our website and need someone to design a very clean modern home page. We have a wireframe for the content and basic layout (see attached). We just need someone to make it look beautiful.

This web page will be hosted on a private server using HTML5. I have developers who will integrate the rotating images and referenced video files - we just need you to focus on the visual elements.

You can take a look at our current website at tavenfold.com for color style guides, logos, etc.

```html
<!DOCTYPE html>
<html lang="en">
<head>
<meta charset="utf-8">
<title>Tavenfold – Home</title>
<link rel="stylesheet" href="https://fonts.googleapis.com/css2?family=Inter:wght@300;400&display=swap">
<style>
  :root {
    --brand-blue: #1f5fae;
    --footer-navy: #1b3453;
    --ink: #111111;
    --body-ink: #333333;
    --white: #ffffff;
    --quote-ink: #dce7f5;
    --star: #f5a623;
    --cta-green: #79cc3c;
  }
  * { box-sizing: border-box; margin: 0; padding: 0; }
  html, body { width: 1200px; height: 1200px; overflow: hidden; }
  body { font-family: "Inter", "Helvetica Neue", Arial, sans-serif; background: var(--white); position: relative; }

  .testimonials { position: absolute; left: 0; top: 0; width: 1200px; height: 517px; background: var(--brand-blue); color: var(--white); }
  .section-title { position: absolute; left: 132px; font-weight: 300; font-size: 32px; letter-spacing: -0.2px; }
  .testimonials .section-title { top: 90px; }
  .quote { position: absolute; left: 132px; top: 153px; width: 430px; font-weight: 300; font-size: 14.5px; line-height: 27.6px; color: var(--quote-ink); letter-spacing: -0.2px; }
  .reviewer { position: absolute; left: 134px; top: 316px; font-weight: 300; font-size: 18px; line-height: 23px; }
  .rating { position: absolute; left: 131px; top: 371px; display: flex; gap: 2px; }

  .photo { position: absolute; left: 618px; width: 496px; height: 330px; }
  .photo-handshake { top: 94px; background: linear-gradient(135deg, #e9e6e0 0%, #c9c4bc 40%, #2a2f3a 60%, #f1efec 100%); }
  .photo-team { top: 614px; background: linear-gradient(120deg, #8d919a 0%, #c8c4be 40%, #d9d6d2 55%, #23386d 80%, #2a3f78 100%); }

  .assessment { position: absolute; left: 0; top: 517px; width: 1200px; height: 521px; color: var(--ink); }
  .assessment .section-title { top: 92px; left: 133px; }
  .assessment .tagline { position: absolute; left: 134px; top: 137px; font-weight: 300; font-size: 22px; }
  .assessment .intro { position: absolute; left: 134px; top: 192px; width: 460px; font-weight: 300; font-size: 14.5px; line-height: 27.6px; color: var(--body-ink); letter-spacing: -0.2px; }
  .cta { position: absolute; left: 133px; top: 384px; width: 130px; height: 35px; border-radius: 5px; background: var(--cta-green); color: var(--white); font-size: 12.5px; display: flex; align-items: center; justify-content: center; text-decoration: none; }

  .site-footer { position: absolute; left: 0; top: 1038px; width: 1200px; height: 162px; background: var(--footer-navy); color: var(--white); font-size: 11.5px; }
  .footer-link { position: absolute; }
</style>
</head>
<body>
  <section class="testimonials">
    <h2 class="section-title">Listen to Our Customers!</h2>
    <p class="quote">“We knew we had a problem with skyrocketing Corvane costs, but did not know how to fix it. These guys are complete professionals and know exactly what they are doing. Within just a few short months Tavenfold reduced my monthly Corvane bill by over 60% and I could not be happier!”</p>
    <p class="reviewer">Marcus Hale<br>Cloud Engineer</p>
    <svg class="rating" width="130" height="26" viewBox="0 0 130 26" aria-label="Five stars">
      <g fill="none" stroke="var(--star)" stroke-width="3.2" stroke-linecap="round">
        <g transform="translate(13 13)"><path d="M0-11V11M-9.5-5.5L9.5 5.5M-9.5 5.5L9.5-5.5"/></g>
        <g transform="translate(39 13)"><path d="M0-11V11M-9.5-5.5L9.5 5.5M-9.5 5.5L9.5-5.5"/></g>
        <g transform="translate(65 13)"><path d="M0-11V11M-9.5-5.5L9.5 5.5M-9.5 5.5L9.5-5.5"/></g>
        <g transform="translate(91 13)"><path d="M0-11V11M-9.5-5.5L9.5 5.5M-9.5 5.5L9.5-5.5"/></g>
        <g transform="translate(117 13)"><path d="M0-11V11M-9.5-5.5L9.5 5.5M-9.5 5.5L9.5-5.5"/></g>
      </g>
    </svg>
    <div class="photo photo-handshake" role="img" aria-label="Photo: business people shaking hands across a meeting table in a bright office"></div>
  </section>

  <section class="assessment">
    <h2 class="section-title">Free Assessment</h2>
    <p class="tagline">No Risk * Real Cost Savings Estimate</p>
    <p class="intro">Wondering if Tavenfold is a good fit for your organization?<br>Toke the guess work out of it and sign for a free assessment. Our team of cloud analysts will work with you to perform a free assessment of your Corvane environment, including the specific cost saving opportunities they identified and the potential annual savings.</p>
    <a class="cta" href="#">Free Assessment</a>
  </section>
  <div class="photo photo-team" role="img" aria-label="Photo: smiling team seated along a conference table with laptops"></div>

  <footer class="site-footer">
    <span class="footer-link" style="left:74px;top:29px">Company</span>
    <span class="footer-link" style="left:74px;top:55px">About Us</span>
    <span class="footer-link" style="left:74px;top:81px">Contact Us</span>
    <span class="footer-link" style="left:232px;top:32px">Product</span>
    <span class="footer-link" style="left:232px;top:59px">Solutions</span>
    <span class="footer-link" style="left:232px;top:89px">Features</span>
    <span class="footer-link" style="left:232px;top:114px">Pricing</span>
    <span class="footer-link" style="left:232px;top:139px">FAQ</span>
    <span class="footer-link" style="left:372px;top:32px">Customer</span>
    <span class="footer-link" style="left:372px;top:55px">Sales</span>
    <span class="footer-link" style="left:372px;top:79px">Support</span>
    <span class="footer-link" style="left:518px;top:32px">Partners</span>
    <span class="footer-link" style="left:518px;top:55px">Become a Reseller</span>
    <span class="footer-link" style="left:518px;top:79px">Portal Login</span>
  </footer>
</body>
</html>
```